I want our new logo design to guide the colors and look of the home page. I want it to be vibrant and contemporary. We are a new religious education publishing company. I would like any colors used to describe the product below to be bright and cheerful, but also to look good with our logo colors
On our home page we are introducing a new product for second graders. The product name should look child friendly, but not silly. If there is a way to add reverence to the words FIRST RECONCILIATION and FIRST EUCHARIST, and still make it look like it is a product for children, that would be great.
The product will be called:
Wayfinder Gathering Set for the Welcoming Room
FIRST RECONCILIATION
FIRST EUCHARIST
THE PRODUCT DESCRIPTION SHOULD BE AS FOLLOWS
Field tested and designed for the special needs inclusive classroom
Kit includes high impact visuals, hands-on activities, manipulatives, games, and other teaching aids for total engagement of ALL students
Detailed catechist lesson plans to maximize learning and retention
Cost effective reusable kit
Bilingual
Somewhere it should say COMING SOON, because the product is not ready yet, but we are promoting it. I don't have a picture of this product yet, but above the product description, we need an empty box that we'll use when we're ready to upload the picture of the kit.
There should also be a statement near the product description that says: To learn more about the Wayfinder Set for the Welcoming Room, click here.
Web page links:
About Us
Products
Resources
Contact Us
I would also like a few links to be featured on the home page:
Lanterns Along the Young Road....learn more
"What Calls Us Home?"....learn more
Could It Be Something Else Entirely?...learn more
The Map and the Path...learn more
Open Table Storytelling
I have increased my budget and clarified my brief so that it's easier to understand. It's basically just a home page and a template for the other pages. There is no content on the other web pages that you have to work on. I just need a well designed home page and a nice template for the other pages.
Reason: I am extending the deadline for 2 days so that templates can be designed for 5 additional web pages. Please make each template a little different from the way you designed the home page. These pages can have blank picture boxes and dummy text to save you time. I am only interested in layout for the addtional pages. Thank you!
We've made a selection and wanted to thank all of you for your wonderful designs!

```html
<!DOCTYPE html>
<html lang="en">
<head>
<meta charset="utf-8">
<title>Harbor Lamp Catechetics</title>
<link rel="stylesheet" href="https://fonts.googleapis.com/css2?family=Open+Sans:wght@300;400&family=Source+Sans+3:wght@400;600&family=Oswald:wght@300;400&family=Arimo&display=swap">
<style>
  :root {
    --brand-red: #b5121b;
    --brand-red-deep: #8e0c14;
    --brand-orange: #f39200;
    --ink: #3d3d3d;
    --ink-soft: #666666;
    --muted: #9a9a9a;
    --panel-grey: #e7e7e7;
    --page-grey: #f7f7f7;
    --white: #ffffff;
  }
  * { box-sizing: border-box; margin: 0; padding: 0; }
  html, body { width: 1200px; height: 1146px; overflow: hidden; background: var(--white); }
  body { position: relative; font-family: "Source Sans 3", Arial, sans-serif; color: var(--ink); }
  a { text-decoration: none; color: inherit; }

  /* Header */
  .site-header { position: absolute; left: 0; top: 0; width: 1200px; height: 155px; }
  .brand-name { position: absolute; left: 40px; top: 74px; font-family: "Source Sans 3", sans-serif; font-weight: 600; font-size: 31px; line-height: 36px; color: var(--brand-red); letter-spacing: -0.3px; white-space: nowrap; }
  .account-links { position: absolute; left: 768px; top: 61px; font-size: 14px; font-weight: 600; color: var(--ink-soft); }
  .search-box { position: absolute; left: 906px; top: 49px; width: 262px; height: 38px; border: 1px solid #d6d6d6; background: var(--white); }
  .search-box span { position: absolute; left: 9px; top: 10px; font-family: "Arimo", sans-serif; font-size: 13px; color: #999; }
  .search-box svg { position: absolute; right: 6px; top: 5px; }
  .main-nav { position: absolute; top: 106px; left: 0; font-family: "Oswald", sans-serif; font-weight: 300; font-size: 19px; color: #111; }
  .main-nav a { position: absolute; white-space: nowrap; }
  .main-nav .is-active { color: var(--brand-red); }

  /* Hero */
  .hero { position: absolute; left: 0; top: 155px; width: 1200px; height: 470px; background: var(--page-grey); }
  .hero-titles { position: absolute; left: 0; top: 14px; width: 611px; height: 442px; background: var(--panel-grey); }
  .hero-titles h1 { position: absolute; left: 78px; top: 148px; font-family: "Open Sans", sans-serif; font-weight: 300; font-size: 42px; line-height: 57px; letter-spacing: 0.5px; }
  .hero-titles .line-one { display: block; color: var(--ink-soft); }
  .hero-titles .line-two { display: block; color: var(--brand-orange); }
  .hero-promo { position: absolute; left: 611px; top: 0; width: 589px; height: 470px;
    background: radial-gradient(ellipse 75% 70% at 55% 35%, #b8141f 0%, #a8111a 55%, var(--brand-red-deep) 100%); color: var(--white); }
  .hero-promo h2 { position: absolute; left: 0; width: 589px; top: 196px; text-align: center; font-family: "Open Sans", sans-serif; font-weight: 300; font-size: 50px; letter-spacing: 1px; }
  .hero-promo p { position: absolute; left: 59px; top: 437px; font-family: "Arimo", sans-serif; font-size: 13px; white-space: nowrap; }
  .hero-promo p a { color: #ffd24a; }

  /* Featured links */
  .feature-links { position: absolute; left: 71px; top: 666px; list-style: none; }
  .feature-links li { position: absolute; left: 0; white-space: nowrap; }
  .feature-links h3 { font-size: 16.5px; font-weight: 600; color: var(--ink); text-transform: uppercase; letter-spacing: 0.1px; }
  .feature-links a.learn-more { display: block; margin: 2px 0 0 1px; font-size: 12.5px; font-weight: 600; color: var(--muted); }

  /* Product points */
  .product-points { position: absolute; left: 627px; top: 684px; width: 560px; list-style: none; }
  .product-points li { position: relative; padding-left: 26px; font-size: 16px; font-weight: 600; line-height: 39.5px; color: var(--brand-red); }
  .product-points li::before { content: ""; position: absolute; left: 0; top: 12px; width: 16px; height: 16px; background: var(--brand-orange); }

  /* Footer */
  .site-footer { position: absolute; left: 0; top: 992px; width: 1200px; height: 154px; background: var(--page-grey); font-family: "Arimo", sans-serif; font-size: 13.5px; color: #555; }
  .site-footer .legal { position: absolute; left: 40px; top: 41px; }
  .footer-nav a { position: absolute; top: 70px; }
  .footer-nav .is-active { color: var(--brand-red); }
</style>
</head>
<body>
  <header class="site-header">
    <div class="brand-name">Harbor Lamp Catechetics</div>
    <div class="account-links"><a href="#">Login</a> | <a href="#">Sign up</a></div>
    <div class="search-box">
      <span>Search Here</span>
      <svg width="28" height="28" viewBox="0 0 28 28" aria-hidden="true">
        <circle cx="11" cy="11" r="8" fill="none" stroke="#c8c8c8" stroke-width="3"/>
        <line x1="17" y1="17" x2="25" y2="25" stroke="#c8c8c8" stroke-width="5" stroke-linecap="round"/>
      </svg>
    </div>
    <nav class="main-nav">
      <a href="#" class="is-active" style="left:771px">ABOUT US</a>
      <a href="#" style="left:876px">PRODUCTS</a>
      <a href="#" style="left:980px">RESOURCES</a>
      <a href="#" style="left:1087px">CONTACT US</a>
    </nav>
  </header>

  <section class="hero">
    <div class="hero-titles">
      <h1><span class="line-one">FIRST RECONCILIATION</span><span class="line-two">FIRST EUCHARIST</span></h1>
    </div>
    <div class="hero-promo">
      <h2>COMING SOON</h2>
      <p>To learn more about the Wayfinder Set for the Welcoming Room, <a href="#">click here.</a></p>
    </div>
  </section>

  <ul class="feature-links">
    <li style="top:0"><h3>Lanterns Along the Young Road</h3><a class="learn-more" href="#">Learn More</a></li>
    <li style="top:58px"><h3>What Calls Us Home?</h3><a class="learn-more" href="#">Learn More</a></li>
    <li style="top:116px"><h3>Could It Be Something Else Entirely?</h3><a class="learn-more" href="#">Learn More</a></li>
    <li style="top:174px"><h3>The Map and the Path</h3><a class="learn-more" href="#">Learn More</a></li>
    <li style="top:232px"><h3>Open Table Storytelling</h3><a class="learn-more" href="#" style="margin-top:6px">Learn More</a></li>
  </ul>

  <ul class="product-points">
    <li>Field tested and designed for the special needs inclusive classroom</li>
    <li>Kit includes high impact visuals, hands-on activities, manipulatives, games, and other teaching aids for total engagement of ALL students</li>
    <li>Detailed catechist lesson plans to maximize learning and retention</li>
    <li>Cost effective reusable kit</li>
    <li>Bilingual</li>
  </ul>

  <footer class="site-footer">
    <p class="legal">Copyright Harbor Lamp Catechetics&nbsp; 2011 All rights reserved &nbsp;| Please review our Privacy Policy and Terms and Conditions.</p>
    <nav class="footer-nav">
      <a href="#" class="is-active" style="left:42px">About Us</a>
      <a href="#" style="left:135px">Products</a>
      <a href="#" style="left:223px">Resources</a>
      <a href="#" style="left:317px">Contact Us</a>
    </nav>
  </footer>
</body>
</html>
```